Marlowe Tessin Real Estate Business Cards
Professional
Marlowe Tessin
Broker
782 W. Larkspur Ave, Suite 315
Beverly Hills, CA 90210
marlowe@marlowetessinrealestate.com
www.marlowetessinrealestate.com
These comments may or may not be included on the back of the card...
Menu of Services-
Investor Services
1% Listings for Flips
Rehab Management
Auction Services
Bidding
Tax & Title Review
Daily Auction Lists
Property Management Services
Leasing
Maintenance
Evictions
Real Estate Services
Buyers/Sellers
REO Specialists
BPO's
Notary
I'm open to ideas on what to have on either side. I'd like to have my picture and my logo on the card and it may or may not be on the same side. I'm also open to adding comments about services I offer (which I included above) but not sure if it works or not.
EPS Version of the logo
AI Version of the logo
JPG Version of the logo
GIF Version of the logo
My Headshot 1
My Headshot 2

```html
<!DOCTYPE html>
<html lang="en">
<head>
<meta charset="utf-8">
<title>Marlowe Tessin Real Estate Business Cards</title>
<link href="https://fonts.googleapis.com/css2?family=Open+Sans:wght@400;600;700&display=swap" rel="stylesheet">
<style>
  :root {
    --bg: #eef1f2;
    --card-white: #ffffff;
    --teal: #3fb6c2;
    --teal-dark: #1e9aa8;
    --teal-deep: #17808c;
    --teal-light: #c9eef1;
    --ink: #3c4a52;
    --ink-soft: #6b7a82;
    --heading: #3a4650;
    --service-head: #10444d;
    --photo: #6b4a3c;
  }
  * { margin: 0; padding: 0; box-sizing: border-box; }
  html, body { width: 1200px; height: 893px; overflow: hidden; }
  body {
    background: var(--bg);
    font-family: "Open Sans", Arial, sans-serif;
    color: var(--ink);
    position: relative;
  }
  .card {
    position: absolute;
    width: 560px;
    height: 320px;
    border-radius: 4px;
    box-shadow: 0 10px 28px rgba(0,0,0,0.18);
    overflow: hidden;
  }

  /* Front */
  .card-front { left: 90px; top: 100px; background: var(--card-white); }
  .front-band {
    position: absolute; left: 0; right: 0; bottom: 0; height: 30px;
    background: linear-gradient(90deg, var(--teal-dark), var(--teal));
  }
  .front-band::before {
    content: ""; position: absolute; left: 0; right: 0; top: -6px; height: 3px;
    background: var(--teal-light);
  }
  .brand {
    position: absolute; left: 40px; top: 110px;
    display: flex; align-items: center; gap: 10px;
  }
  .brand-mark { width: 22px; height: 22px; background: var(--teal); flex: none; }
  .brand-name {
    font-size: 17px; font-weight: 600; color: var(--heading); line-height: 1.25;
  }
  .agent { position: absolute; left: 44px; top: 200px; }
  .agent-name { font-size: 24px; font-weight: 600; color: var(--heading); }
  .agent-title { font-size: 17px; color: var(--ink-soft); margin-top: 2px; }
  .divider {
    position: absolute; left: 284px; top: 40px; width: 1px; height: 210px;
    background: var(--teal);
  }
  .headshot {
    position: absolute; left: 418px; top: 22px; width: 102px; height: 108px;
    border: 3px solid var(--teal);
    background: linear-gradient(160deg, #8a6654, var(--photo));
  }
  .contact { position: absolute; left: 304px; top: 148px; list-style: none; }
  .contact li {
    display: flex; align-items: center; gap: 8px;
    font-size: 10.5px; line-height: 19px; color: var(--ink);
  }
  .contact svg { width: 11px; height: 11px; flex: none; fill: var(--teal-dark); }

  /* Back */
  .card-back {
    left: 550px; top: 470px;
    background: radial-gradient(ellipse 300px 160px at 30% 12%, #dff5f7 0%, #8fd5dc 45%, transparent 100%),
                linear-gradient(160deg, var(--teal) 0%, var(--teal-dark) 60%, var(--teal-deep) 100%);
  }
  .menu-title {
    position: absolute; left: 50px; top: 40px;
    font-size: 24px; font-weight: 600; letter-spacing: 1px; color: var(--heading);
  }
  .menu-title::after {
    content: ""; display: block; width: 200px; height: 2px; background: var(--heading); margin-top: 6px;
  }
  .service {
    position: absolute; font-size: 11.5px; line-height: 16px; color: #ffffff;
    text-shadow: 0 1px 2px rgba(0, 60, 70, 0.35);
  }
  .service h3 {
    font-size: 12.5px; font-weight: 700; color: var(--service-head);
    margin-bottom: 2px; text-shadow: none;
  }
  .service-investor { left: 50px; top: 150px; }
  .service-auction { left: 50px; top: 226px; }
  .service-property { left: 310px; top: 76px; }
  .service-realestate { left: 310px; top: 168px; }
</style>
</head>
<body>
  <section class="card card-front" aria-label="Business card front">
    <div class="brand">
      <div class="brand-mark"></div>
      <div class="brand-name">Marlowe Tessin<br>Real Estate</div>
    </div>
    <div class="agent">
      <div class="agent-name">Marlowe Tessin</div>
      <div class="agent-title">Broker</div>
    </div>
    <div class="divider"></div>
    <div class="headshot" role="img" aria-label="Headshot of the broker"></div>
    <ul class="contact">
      <li><svg viewBox="0 0 12 12"><path d="M6 0a4 4 0 0 0-4 4c0 3 4 8 4 8s4-5 4-8a4 4 0 0 0-4-4zm0 5.5A1.5 1.5 0 1 1 6 2.5a1.5 1.5 0 0 1 0 3z"/></svg>782 W. Larkspur Ave, Suite 315</li>
      <li><svg viewBox="0 0 12 12"></svg>Beverly Hills, CA 90210</li>
      <li><svg viewBox="0 0 12 12"><path d="M2.5 0 4.5 2.5 3.5 4c.8 1.8 2.2 3.2 4 4l1.5-1L12 9l-1.5 2.5C5 11 1 7 .5 1.5z"/></svg>310-555-0147</li>
      <li><svg viewBox="0 0 12 12"><path d="M0 2h12v8H0zm1 1v.4l5 3.4 5-3.4V3zm0 1.6V9h10V4.6L6 8z"/></svg>marlowe@marlowetessinrealestate.com</li>
      <li><svg viewBox="0 0 12 12"><path d="M6 0a6 6 0 1 0 0 12A6 6 0 0 0 6 0zm0 1.2c.6.6 1.2 1.9 1.4 3.3H4.6C4.8 3.1 5.4 1.8 6 1.2zM1.3 5.5h2.3c0 1 .2 2 .5 2.9H2a4.8 4.8 0 0 1-.7-2.9zm3.3 0h2.8c0 1-.2 2-.6 2.9H5.2c-.4-.9-.6-1.9-.6-2.9zm3.8 0h2.3a4.8 4.8 0 0 1-.7 2.9H7.9c.3-.9.5-1.9.5-2.9z"/></svg>www.marlowetessinrealestate.com</li>
    </ul>
    <div class="front-band"></div>
  </section>

  <section class="card card-back" aria-label="Business card back">
    <h2 class="menu-title">MENU OF SERVICES</h2>
    <div class="service service-investor">
      <h3>Investor Services</h3>
      1% Listings for Flips<br>Rehab Management
    </div>
    <div class="service service-auction">
      <h3>Auction Services</h3>
      Bidding<br>Tax &amp; Title Review<br>Daily Auction Lists
    </div>
    <div class="service service-property">
      <h3>Property Management Services</h3>
      Leasing<br>Maintenance<br>Evictions
    </div>
    <div class="service service-realestate">
      <h3>Real Estate Services</h3>
      Buyers/Sellers<br>REO Specialists<br>BPO's<br>Notary
    </div>
  </section>
</body>
</html>
```